Personal training studio poster / postcard

We need a poster / postcard design to advertise our recently established personal training studio - details and logo in the attached file. Logo file also provided.

We are flexible on format. Prefer the use of pictures in the design.

Training

```html
<!DOCTYPE html>
<html lang="en">
<head>
<meta charset="utf-8">
<title>Ashcombe Strength Studio – Class Poster</title>
<link rel="stylesheet" href="https://fonts.googleapis.com/css2?family=Stardos+Stencil:wght@700&family=Roboto+Condensed:wght@400&display=swap">
<style>
  :root {
    --bg-dark: #1c1d20;
    --bg-mid: #3a3b3f;
    --panel-dark: #2b2d38;
    --panel-mid: #454856;
    --red: #e8262b;
    --red-soft: #f0646a;
    --black: #111114;
    --steel: #c3c6cd;
    --steel-dark: #8d9099;
    --type-light: #d9dbe0;
    --logo-silver: #d4d6db;
  }
  html, body {
    margin: 0;
    padding: 0;
    overflow: hidden;
    background: var(--bg-dark);
  }
  .poster {
    position: relative;
    width: 933px;
    height: 1200px;
    overflow: hidden;
    background: radial-gradient(ellipse at 55% 35%, var(--bg-mid) 0%, #2a2b2f 45%, var(--bg-dark) 100%);
  }
  .athlete-photo {
    position: absolute;
    left: 373px;
    top: 0;
    width: 560px;
    height: 806px;
    background:
      radial-gradient(ellipse at 58% 55%, #1f5fcf 0%, #1f5fcf 14%, transparent 30%),
      radial-gradient(ellipse at 55% 45%, #b07a5c 0%, #8a5a43 40%, transparent 72%);
  }
  .shapes {
    position: absolute;
    inset: 0;
    width: 933px;
    height: 1200px;
  }
  .brand {
    position: absolute;
    left: 40px;
    top: 88px;
    font-family: "Stardos Stencil", "Arial Black", sans-serif;
    font-weight: 700;
    color: var(--logo-silver);
    font-size: 44px;
    line-height: 44px;
    letter-spacing: 1px;
  }
  .brand-line-small {
    display: block;
    font-size: 28px;
    letter-spacing: 4px;
  }
  .panel-copy {
    position: absolute;
    left: 254px;
    top: 540px;
    width: 640px;
    transform: rotate(38deg);
    transform-origin: left top;
  }
  .studio-name {
    margin: 0;
    font-family: "Stardos Stencil", "Arial Black", sans-serif;
    font-weight: 700;
    color: var(--steel);
    text-shadow: 2px 2px 0 var(--steel-dark);
    line-height: 1;
  }
  .studio-name-main {
    display: block;
    font-size: 76px;
    letter-spacing: 6px;
  }
  .studio-name-sub {
    display: block;
    font-size: 46px;
    letter-spacing: 3px;
    margin-left: -8px;
    margin-top: 2px;
  }
  .class-schedule {
    list-style: none;
    margin: 34px 0 0 -70px;
    padding: 0;
    width: 420px;
    font-family: "Roboto Condensed", "Arial Narrow", sans-serif;
    font-size: 20px;
    line-height: 27px;
    letter-spacing: 1px;
    color: var(--type-light);
    text-transform: uppercase;
  }
  .class-schedule li {
    margin-bottom: 12px;
  }
</style>
</head>
<body>
<main class="poster">
  <div class="athlete-photo" role="img" aria-label="Photo of a female athlete in a blue sports bra, hand on hip, against a dark grunge backdrop"></div>

  <svg class="shapes" viewBox="0 0 625 804" preserveAspectRatio="none" aria-hidden="true">
    <defs>
      <linearGradient id="panel-fill" x1="0" y1="0" x2="1" y2="1">
        <stop offset="0" stop-color="var(--panel-mid)"/>
        <stop offset="1" stop-color="var(--panel-dark)"/>
      </linearGradient>
      <linearGradient id="red-fade" x1="0" y1="0" x2="1" y2="0">
        <stop offset="0" stop-color="var(--red)"/>
        <stop offset="1" stop-color="var(--red-soft)"/>
      </linearGradient>
    </defs>

    <!-- left side band and stripes -->
    <polygon class="side-band" points="0,345 150,330 200,360 130,470 0,460" fill="#26272c"/>
    <g class="side-stripes" stroke="#6b6d74" stroke-width="3">
      <line x1="10" y1="395" x2="40" y2="365"/>
      <line x1="22" y1="400" x2="52" y2="370"/>
      <line x1="34" y1="405" x2="64" y2="375"/>
      <line x1="46" y1="410" x2="76" y2="380"/>
      <line x1="58" y1="415" x2="88" y2="385"/>
    </g>

    <!-- main copy panel -->
    <polygon class="copy-panel" points="200,322 320,318 548,480 520,640 300,705 60,690 70,470" fill="url(#panel-fill)"/>
    <polygon class="panel-edge-red" points="232,318 340,320 565,470 545,482 330,330" fill="url(#red-fade)"/>
    <polygon class="panel-facet" points="60,600 300,705 60,690" fill="#363844"/>

    <!-- lower left red block -->
    <polygon class="corner-red" points="0,680 140,650 330,730 300,804 0,804" fill="url(#red-fade)"/>
    <polygon class="corner-dark" points="0,720 120,700 230,804 0,804" fill="#1e1f25"/>

    <!-- lower right shards -->
    <polygon class="shard-dark" points="370,804 520,650 625,560 625,804" fill="var(--black)"/>
    <polygon class="shard-red" points="560,530 625,540 625,600 595,665" fill="var(--red)"/>
    <polygon class="shard-red-low" points="455,640 530,610 470,760" fill="var(--red)"/>
    <polygon class="shard-white" points="538,690 578,668 568,700" fill="#e9eaec"/>
  </svg>

  <div class="brand">ASHCOMBE<span class="brand-line-small">STRENGTH STUDIO</span></div>

  <section class="panel-copy">
    <h1 class="studio-name">
      <span class="studio-name-main">ASHCOMBE</span>
      <span class="studio-name-sub">STRENGTH STUDIO</span>
    </h1>
    <ul class="class-schedule">
      <li>Power Circuit – Tuesdays 6:15am</li>
      <li>Boxing + MMA – Tuesdays and Thursdays 6:15pm</li>
      <li>Yoga – Saturdays 9am</li>
    </ul>
  </section>
</main>
</body>
</html>
```